New Business Card Design Project

Need a design that will create an impact / strong impression towards our clients for our business. We are in the lighting business and we do lighting retrofits for large commercial to industrial clientele.

Target Market(s)

Lighting Industry

Industry/Entity Type

Business

Other font styles liked:
• we would like to use the font on our logo, not sure what it is though..

Requirements
Must have
• Our logo.
Nice to have
• We are open to suggestions that have to do with lighting.

```html
<!DOCTYPE html>
<html lang="en">
<head>
<meta charset="utf-8">
<title>Brightway Lighting Partners – Business Card</title>
<link rel="stylesheet" href="https://fonts.googleapis.com/css2?family=Source+Sans+3:wght@400;600;700&display=swap">
<style>
  :root {
    --bg: #3b3431;
    --card: #ffffff;
    --green: #1e9a34;
    --green-light: #3cc04f;
    --green-dark: #146b26;
    --ink: #111111;
    --shadow: rgba(0, 0, 0, 0.45);
  }
  * { margin: 0; padding: 0; box-sizing: border-box; }
  html, body {
    width: 1200px;
    height: 844px;
    overflow: hidden;
    background: var(--bg);
    font-family: "Source Sans 3", "Myriad Pro", Arial, sans-serif;
  }
  .canvas {
    position: relative;
    width: 1200px;
    height: 844px;
  }
  .card {
    position: absolute;
    top: 272px;
    width: 520px;
    height: 300px;
    background: var(--card);
    box-shadow: 0 14px 30px var(--shadow);
    overflow: hidden;
  }
  .card--back { left: 50px; }
  .card--front { left: 630px; }

  /* Back side: contact details */
  .band {
    position: absolute;
    left: 0;
    width: 100%;
    background: linear-gradient(to bottom, var(--green-light), var(--green));
  }
  .band--top { top: 0; height: 14px; }
  .band--bottom { bottom: 0; height: 18px; background: linear-gradient(to bottom, var(--green), var(--green-light)); }

  .person {
    position: absolute;
    top: 62px;
    left: 0;
    width: 100%;
    text-align: center;
  }
  .person__name {
    display: inline-block;
    color: var(--green);
    font-weight: 600;
    font-size: 17px;
    letter-spacing: 0.3px;
    text-transform: uppercase;
    padding: 0 4px 2px;
    border-bottom: 1px solid var(--green);
  }
  .person__title {
    color: var(--ink);
    font-size: 14px;
    margin-top: 1px;
  }
  .contact {
    position: absolute;
    top: 152px;
    left: 0;
    width: 100%;
    text-align: center;
    color: var(--ink);
    font-size: 14px;
    line-height: 17px;
    list-style: none;
  }
  .contact__address {
    margin-top: 10px;
    font-size: 15px;
  }

  /* Front side: company name */
  .tab {
    position: absolute;
    width: 26px;
    height: 46px;
    background: linear-gradient(to right, var(--green-dark), var(--green-light));
  }
  .tab--left { left: 0; top: 128px; }
  .tab--right { right: 0; top: 40px; background: linear-gradient(to left, var(--green-dark), var(--green-light)); }

  .company {
    position: absolute;
    top: 96px;
    left: 0;
    width: 100%;
    text-align: center;
    color: var(--green);
    font-weight: 700;
  }
  .company__mark {
    display: inline-flex;
    align-items: center;
    gap: 12px;
    font-size: 40px;
    letter-spacing: 1px;
    line-height: 1;
  }
  .company__square {
    width: 22px;
    height: 22px;
    background: var(--green);
  }
  .company__legal {
    display: inline-block;
    margin-top: 8px;
    padding-top: 4px;
    border-top: 1px solid var(--green);
    font-size: 12px;
    letter-spacing: 1.2px;
    text-transform: uppercase;
  }
</style>
</head>
<body>
<main class="canvas">
  <section class="card card--back" aria-label="Business card, contact side">
    <div class="band band--top"></div>
    <div class="person">
      <div class="person__name">Daniel Reyes</div>
      <div class="person__title">Managing Director</div>
    </div>
    <ul class="contact">
      <li>044-456-7890</li>
      <li>123-456-7890</li>
      <li>infoname@yourwebsite.com</li>
      <li>www.website.com</li>
      <li class="contact__address">1234 Address Tag Line | Country Name, AB | 123456</li>
    </ul>
    <div class="band band--bottom"></div>
  </section>

  <section class="card card--front" aria-label="Business card, company side">
    <div class="tab tab--right"></div>
    <div class="tab tab--left"></div>
    <div class="company">
      <div class="company__mark">BRIGHTWAY <span class="company__square"></span></div><br>
      <span class="company__legal">Brightway Lighting Partners, LLC</span>
    </div>
  </section>
</main>
</body>
</html>
```